KORBALT

The business want a professional looking business card. We have a scetch we will add but want the extra upgrade, and would like more suggestions for variations of our business cards.

```html
<!DOCTYPE html>
<html lang="en">
<head>
<meta charset="utf-8">
<title>KORBALT business card</title>
<link href="https://fonts.googleapis.com/css2?family=Playfair+Display:wght@700&family=Montserrat:wght@400;500;600&display=swap" rel="stylesheet">
<style>
  :root {
    --backdrop: #45301f;
    --card: #ffffff;
    --gold: #d9a23e;
    --gold-light: #fcd06c;
    --gold-deep: #d0943a;
    --gold-faint: #f6e3bd;
    --ink: #4a4a4a;
    --grey: #7a7a7a;
  }
  * { box-sizing: border-box; margin: 0; padding: 0; }
  html, body { width: 1126px; height: 1200px; overflow: hidden; }
  body {
    background: var(--backdrop);
    font-family: "Montserrat", sans-serif;
    position: relative;
  }
  .card {
    position: absolute;
    top: 455px;
    width: 472px;
    height: 290px;
    background: var(--card);
    border-radius: 24px;
    overflow: hidden;
  }
  .card--front { left: 78px; }
  .card--back { left: 576px; }
  .gold-band {
    position: absolute;
    left: 0; right: 0; bottom: 0;
    height: 37px;
    background: linear-gradient(90deg, var(--gold-deep), var(--gold-light) 48%, var(--gold-deep));
  }
  .brand {
    position: absolute;
    text-align: center;
    transform: translateX(-50%);
  }
  .brand__dot {
    display: block;
    margin: 0 auto;
    border-radius: 50%;
    background: var(--gold);
  }
  .brand__name {
    font-family: "Playfair Display", serif;
    font-weight: 700;
    color: var(--gold);
    letter-spacing: 0.04em;
    line-height: 1;
  }
  .brand__tagline {
    color: var(--grey);
    letter-spacing: 0.16em;
    line-height: 1;
  }
  .card--front .brand { left: 106px; top: 48px; }
  .card--front .brand__dot { width: 30px; height: 30px; margin-bottom: 22px; }
  .card--front .brand__name { font-size: 25px; }
  .card--front .brand__tagline { font-size: 12px; margin-top: 4px; }
  .card--back .brand { left: 236px; top: 82px; }
  .card--back .brand__dot { width: 40px; height: 40px; margin-bottom: 36px; }
  .card--back .brand__name { font-size: 34px; }
  .card--back .brand__tagline { font-size: 17px; margin-top: 5px; }
  .watermark {
    position: absolute;
    left: 305px; top: 0;
    width: 162px; height: 162px;
    border-radius: 50%;
    background: var(--gold-faint);
    opacity: 0.75;
  }
  .holder {
    position: absolute;
    left: 32px; top: 186px;
    font-size: 15px;
    line-height: 18px;
    color: var(--ink);
  }
  .holder__company { color: var(--gold); font-weight: 600; }
  .contact {
    position: absolute;
    left: 244px; top: 173px;
  }
  .contact__rail {
    position: absolute;
    left: 0; top: 2px;
    width: 17px; height: 72px;
    border-radius: 9px;
    background: var(--gold);
  }
  .contact__rail svg { display: block; margin: 4px auto 0; }
  .contact__list {
    list-style: none;
    margin-left: 22px;
    font-size: 15px;
    color: var(--ink);
    line-height: 22px;
  }
</style>
</head>
<body>
  <section class="card card--front">
    <div class="watermark" aria-hidden="true"></div>
    <div class="brand">
      <span class="brand__dot"></span>
      <div class="brand__name">KORBALT</div>
      <div class="brand__tagline">SINCE 2026</div>
    </div>
    <div class="holder">
      <div class="holder__company">KORBALT A HAUGEN</div>
      <div>CEO &amp; Founder</div>
      <div>Anders Lund Haugen</div>
    </div>
    <div class="contact">
      <div class="contact__rail">
        <svg width="11" height="11" viewBox="0 0 24 24" aria-hidden="true"><path fill="#fff" d="M6.6 10.8a15 15 0 0 0 6.6 6.6l2.2-2.2c.3-.3.7-.4 1-.2 1.1.4 2.3.6 3.6.6.6 0 1 .4 1 1V20c0 .6-.4 1-1 1A17 17 0 0 1 3 4c0-.6.4-1 1-1h3.5c.6 0 1 .4 1 1 0 1.3.2 2.5.6 3.6.1.3 0 .7-.2 1z"/></svg>
        <svg width="11" height="11" viewBox="0 0 24 24" style="margin-top:11px" aria-hidden="true"><path fill="none" stroke="#fff" stroke-width="2" d="M3 6h18v12H3zM3 6l9 7 9-7"/></svg>
        <svg width="11" height="11" viewBox="0 0 24 24" style="margin-top:11px" aria-hidden="true"><g fill="none" stroke="#fff" stroke-width="2"><circle cx="12" cy="12" r="9"/><path d="M3 12h18M12 3c3 3 3 15 0 18M12 3c-3 3-3 15 0 18"/></g></svg>
      </div>
      <ul class="contact__list">
        <li>004791234567</li>
        <li>korbalt.llc@mailbox.com</li>
        <li>www.korbalt.llc</li>
      </ul>
    </div>
    <div class="gold-band"></div>
  </section>

  <section class="card card--back">
    <div class="brand">
      <span class="brand__dot"></span>
      <div class="brand__name">KORBALT</div>
      <div class="brand__tagline">SINCE 2026</div>
    </div>
    <div class="gold-band"></div>
  </section>
</body>
</html>
```